Brindle Gardenworks Business Card

An eye catching, yet simple business card that includes;

1. our logo
2. office phone - 5127730194
3. email - brindlegardenworks@mailnest.example
4. website - www.brindlegardenworks.example
5. instagram - @brindlegardenworksrvt

```html
<!DOCTYPE html>
<html lang="en">
<head>
<meta charset="utf-8">
<title>Brindle Gardenworks Business Card</title>
<link href="https://fonts.googleapis.com/css2?family=Montserrat:wght@400;500;700;800&display=swap" rel="stylesheet">
<style>
  :root {
    --backdrop: #d4d5d1;
    --paper: #ecebe8;
    --copper: #a9652a;
    --ink: #2b2623;
    --night: #1d1a19;
    --pattern-light: #9b9a98;
  }
  html, body {
    margin: 0;
    width: 1200px;
    height: 801px;
    overflow: hidden;
    background: var(--backdrop);
    font-family: "Montserrat", sans-serif;
  }
  .canvas {
    position: relative;
    width: 1200px;
    height: 801px;
  }
  .card {
    position: absolute;
    width: 540px;
    height: 309px;
    box-sizing: border-box;
    border-bottom: 3px solid var(--copper);
    box-shadow: 0 10px 24px rgba(0,0,0,0.18);
  }
  .card-front {
    left: 40px;
    top: 246px;
    background: var(--paper);
  }
  .card-back {
    left: 620px;
    top: 246px;
    background: var(--night);
    overflow: hidden;
  }
  .brand {
    position: absolute;
    right: 34px;
    top: 44px;
    display: flex;
    align-items: center;
    gap: 10px;
  }
  .brand-dot {
    width: 16px;
    height: 16px;
    border-radius: 50%;
    background: var(--copper);
  }
  .brand-name {
    font-weight: 800;
    font-size: 22px;
    color: var(--copper);
    letter-spacing: 0.5px;
  }
  .divider {
    position: absolute;
    left: 30px;
    right: 110px;
    top: 160px;
    height: 1px;
    background: var(--copper);
  }
  .person {
    position: absolute;
    left: 30px;
    top: 110px;
  }
  .person-name {
    margin: 0;
    font-weight: 700;
    font-size: 22px;
    color: var(--copper);
    letter-spacing: 0.5px;
    line-height: 1;
  }
  .person-role {
    margin: 3px 0 0;
    font-size: 13px;
    color: var(--ink);
  }
  .contacts {
    position: absolute;
    left: 30px;
    top: 176px;
    margin: 0;
    padding: 0;
    list-style: none;
    font-size: 13px;
    color: var(--ink);
    line-height: 1.5;
  }
  .contacts li {
    display: flex;
    align-items: center;
    gap: 6px;
  }
  .contacts li.social { margin-top: 10px; }
  .contacts svg {
    width: 11px;
    height: 11px;
    flex: none;
  }
  .pattern {
    position: absolute;
    inset: 0;
    background:
      radial-gradient(ellipse at 85% 10%, var(--pattern-light) 0%, rgba(155,154,152,0.35) 35%, transparent 65%),
      linear-gradient(200deg, #4a4745 0%, var(--night) 60%);
  }
</style>
</head>
<body>
<main class="canvas">
  <section class="card card-front">
    <div class="brand">
      <span class="brand-dot"></span>
      <span class="brand-name">Brindle Gardenworks</span>
    </div>
    <div class="person">
      <h1 class="person-name">REID CALLOW</h1>
      <p class="person-role">Director</p>
    </div>
    <div class="divider"></div>
    <ul class="contacts">
      <li>
        <svg viewBox="0 0 12 12"><path d="M3 1 L5 3.5 L4 5 Q5.5 7.5 7 8 L8.5 7 L11 9 L9.5 11 Q4 10.5 1 3 Z" fill="var(--copper)"/></svg>
        (512) 773 0194
      </li>
      <li>
        <svg viewBox="0 0 12 12"><rect x="1" y="2.5" width="10" height="7" fill="none" stroke="var(--copper)" stroke-width="1.2"/><path d="M1 2.5 L6 6.5 L11 2.5" fill="none" stroke="var(--copper)" stroke-width="1.2"/></svg>
        brindlegardenworks@mailnest.example
      </li>
      <li>
        <svg viewBox="0 0 12 12"><circle cx="6" cy="6" r="5" fill="none" stroke="var(--copper)" stroke-width="1.2"/><path d="M1 6 H11 M6 1 Q3 6 6 11 M6 1 Q9 6 6 11" fill="none" stroke="var(--copper)" stroke-width="1"/></svg>
        www.brindlegardenworks.example
      </li>
      <li class="social">
        <svg viewBox="0 0 12 12"><rect x="1" y="1" width="10" height="10" rx="2" fill="none" stroke="var(--copper)" stroke-width="1.2"/></svg>
        @brindlegardenworksrvt
      </li>
    </ul>
  </section>

  <section class="card card-back">
    <div class="pattern" role="img" aria-label="Repeating pattern of leaping animal silhouettes in glossy black and grey, with one copper silhouette"></div>
  </section>
</main>
</body>
</html>
```